Business Card Design

My company is a Mobile RV Service,...we fix / repair / replace any
and all items on an RV that needs fixing or installing.....Our service goes to the customer, so they don't have to break down their rv from where ever they are at, and work on their unit in place. We also provide warranty service from the industry manufacturers who's products have been installed in the RV's. We also do insurance claims & repairs, & install items that the customer wants additionally installed ..ie: satellite systems, etc..
We accept cash, checks & especially ( all major credit cards )

Reason: 7:30 pm EST...USA,......Not sure how late people work in Australia,.....so ( 1 ) more day for a few finishing touches should be allowed......Thankyou, Dorwinel

Insurance

Bramblecrest Mobile RV Service 904-555-0162 Major credit cards
K.P.L.O. / K.P.E.N. Master Certified R.V. Technician
Licensed / Insured ( The " A " in Bramblecrest BOLD & RED ) also some kind of RV graphic somewhere on the card... The design has to sing !!!!.... Also design will be used for vehicle magnets or
vehicle wrap !!!!....

```html
<!DOCTYPE html>
<html lang="en">
<head>
<meta charset="utf-8">
<title>Bramblecrest Mobile RV Service – Business Card</title>
<link href="https://fonts.googleapis.com/css2?family=Arimo:ital,wght@0,400;0,700;1,700&display=swap" rel="stylesheet">
<style>
  :root {
    --backdrop: #e9e7e4;
    --card: #ffffff;
    --card-edge: #f0f0f0;
    --ink: #2b2b2b;
    --ink-soft: #555555;
    --accent-red: #d8161c;
    --stripe: #d4d4d4;
    --stripe-dark: #bdbdbd;
    --badge-gold: #e6a321;
    --badge-blue: #2f4f9a;
    --badge-green: #2f6b3a;
    --fleet-light: #eef0f2;
    --fleet-mid: #b9bdc2;
    --fleet-dark: #5e5352;
  }
  * { margin: 0; padding: 0; box-sizing: border-box; }
  html, body { width: 1200px; height: 900px; overflow: hidden; }
  body {
    background: var(--backdrop);
    font-family: "Arimo", Arial, sans-serif;
    color: var(--ink);
    position: relative;
  }
  .business-card {
    position: absolute;
    left: 180px; top: 210px;
    width: 840px; height: 480px;
    background: linear-gradient(180deg, var(--card) 0%, var(--card-edge) 100%);
    box-shadow: 0 10px 28px rgba(0,0,0,.25);
    overflow: hidden;
  }
  .title-stripes {
    position: absolute; left: 0; top: 0; width: 840px; height: 130px;
  }
  .company-name {
    position: absolute; left: 36px; top: 18px;
    font-size: 40px; font-weight: 400; color: var(--ink);
    letter-spacing: .5px; white-space: nowrap; line-height: 1;
  }
  .company-name .initial {
    color: var(--accent-red); font-weight: 700; font-size: 92px;
    line-height: 1;
  }
  .phone-row {
    position: absolute; left: 450px; top: 136px; width: 380px; height: 54px;
    display: flex; align-items: center; gap: 10px;
  }
  .phone-stripes { width: 70px; height: 44px; }
  .phone-number {
    color: var(--accent-red); font-weight: 700; font-size: 40px; white-space: nowrap;
  }
  .credential {
    position: absolute; text-align: center;
    font-size: 15px; font-weight: 700; font-style: italic; color: var(--ink);
  }
  .credential svg { display: block; margin: 0 auto 6px; }
  .credential--master { left: 34px; top: 186px; width: 150px; }
  .credential--licensed { left: 200px; top: 150px; width: 160px; }
  .credential--assoc { left: 362px; top: 140px; width: 76px; }
  .payment-list {
    position: absolute; left: 600px; top: 210px; width: 220px;
    display: grid; grid-template-columns: 1fr 1fr; gap: 18px 14px;
  }
  .payment-name {
    font-size: 18px; font-weight: 700; color: var(--ink-soft);
    display: flex; align-items: center; gap: 6px;
  }
  .payment-name::before {
    content: ""; width: 10px; height: 10px; background: var(--stripe-dark);
  }
  .fleet-visual {
    position: absolute; left: 30px; top: 292px; width: 555px; height: 178px;
    background: linear-gradient(100deg, var(--fleet-mid) 0%, var(--fleet-light) 35%, var(--fleet-dark) 60%, var(--fleet-mid) 80%, var(--fleet-light) 100%);
    border-radius: 14px 14px 4px 4px;
    opacity: .9;
  }
</style>
</head>
<body>
  <article class="business-card">
    <svg class="title-stripes" viewBox="0 0 840 130" aria-hidden="true">
      <rect x="0" y="8" width="840" height="4" fill="var(--stripe)"/>
      <rect x="0" y="15" width="840" height="3" fill="var(--stripe)"/>
      <rect x="0" y="118" width="840" height="4" fill="var(--stripe-dark)"/>
      <rect x="0" y="125" width="840" height="3" fill="var(--stripe)"/>
    </svg>
    <h1 class="company-name"><span class="initial">B</span>ramblecrest Mobile RV Service</h1>

    <div class="phone-row">
      <svg class="phone-stripes" viewBox="0 0 70 44" aria-hidden="true">
        <rect x="0" y="8" width="70" height="5" fill="var(--stripe)"/>
        <rect x="0" y="19" width="70" height="5" fill="var(--stripe)"/>
        <rect x="0" y="30" width="70" height="5" fill="var(--stripe)"/>
      </svg>
      <svg width="22" height="22" viewBox="0 0 24 24" aria-hidden="true">
        <path d="M6.6 10.8a15 15 0 0 0 6.6 6.6l2.2-2.2c.3-.3.7-.4 1-.2 1.1.4 2.3.6 3.6.6.6 0 1 .4 1 1V20c0 .6-.4 1-1 1A17 17 0 0 1 3 4c0-.6.4-1 1-1h3.5c.6 0 1 .4 1 1 0 1.3.2 2.5.6 3.6.1.3 0 .7-.2 1z" fill="var(--ink)"/>
      </svg>
      <span class="phone-number">904-555-0162</span>
    </div>

    <div class="credential credential--master">
      <svg width="70" height="56" viewBox="0 0 70 56" aria-hidden="true">
        <circle cx="35" cy="28" r="24" fill="none" stroke="var(--badge-gold)" stroke-width="6"/>
      </svg>
      Master Certified
    </div>
    <div class="credential credential--licensed">
      <svg width="110" height="60" viewBox="0 0 110 60" aria-hidden="true">
        <ellipse cx="55" cy="30" rx="50" ry="26" fill="var(--badge-blue)"/>
      </svg>
      Licensed / Insured
    </div>
    <div class="credential credential--assoc">
      <svg width="68" height="68" viewBox="0 0 72 72" aria-hidden="true">
        <circle cx="36" cy="36" r="32" fill="var(--badge-green)"/>
      </svg>
    </div>

    <div class="payment-list" aria-label="Accepted cards">
      <span class="payment-name">Paywell</span>
      <span class="payment-name">Cardora</span>
      <span class="payment-name">Findly</span>
      <span class="payment-name">Amerivo</span>
    </div>

    <div class="fleet-visual" role="img" aria-label="Three large motorhomes lined up diagonally, silver, black and burgundy coaches"></div>
  </article>
</body>
</html>
```